We need a letterhead design for a new international company based in Luanda, Angola called "Halvorn Corporation". Halvorn Corporation is a multiservice private company. We provides services for the following sectors: Oil & Gas industry, Government, and the Public.

Target Market(s)

Board of directors of the following sectors: Oil & Gas industry, Government, and the Public.

Industry/Entity Type

Government

Requirements
Must have
• Halvorn Corporation logo

```html
<!DOCTYPE html>
<html lang="en">
<head>
<meta charset="utf-8">
<title>Halvorn Corporation — Letterhead</title>
<link href="https://fonts.googleapis.com/css2?family=Exo+2:wght@400;600&display=swap" rel="stylesheet">
<style>
  :root {
    --backdrop: #7f7f7f;
    --paper: #f1f2f5;
    --brand-red: #a3141c;
    --brand-gold: #d9a514;
    --ink: #2a2a2c;
    --ink-soft: #6d6f75;
  }
  html, body {
    margin: 0;
    width: 1200px;
    height: 993px;
    overflow: hidden;
    background: var(--backdrop);
    font-family: "Exo 2", sans-serif;
  }
  .letterhead {
    position: absolute;
    left: 300px;
    top: 72px;
    width: 600px;
    height: 849px;
    background: var(--paper);
    box-shadow: 0 6px 24px rgba(0,0,0,.25);
  }
  .letterhead__band {
    height: 7px;
    background: var(--brand-red);
  }
  .contact {
    position: absolute;
    left: 38px;
    top: 38px;
    margin: 0;
    padding: 0;
    list-style: none;
    font-size: 9px;
    line-height: 13px;
    color: var(--ink-soft);
  }
  .contact__item {
    display: flex;
    align-items: center;
    gap: 6px;
  }
  .contact__icon {
    width: 9px;
    height: 9px;
    flex: none;
  }
  .contact__item--plain { padding-left: 15px; }
  .brand {
    position: absolute;
    right: 44px;
    top: 120px;
    display: flex;
    align-items: center;
    gap: 12px;
  }
  .brand__mark {
    width: 38px;
    height: 38px;
    border-radius: 50%;
    background: var(--brand-gold);
  }
  .brand__name {
    font-weight: 600;
    font-size: 26px;
    letter-spacing: .5px;
    color: var(--ink);
  }
</style>
</head>
<body>
  <main class="letterhead">
    <div class="letterhead__band"></div>

    <ul class="contact">
      <li class="contact__item">
        <svg class="contact__icon" viewBox="0 0 10 10"><circle cx="5" cy="5" r="5" fill="#a3141c"/><path d="M3 2.5l1 .1.5 1.4-.7.5a4 4 0 0 0 1.7 1.7l.5-.7 1.4.5.1 1A1 1 0 0 1 6.5 8 5 5 0 0 1 2 3.5a1 1 0 0 1 1-1z" fill="#fff"/></svg>
        +244 222 410 300
      </li>
      <li class="contact__item">
        <svg class="contact__icon" viewBox="0 0 10 10"><circle cx="5" cy="5" r="5" fill="#a3141c"/><rect x="3.3" y="2" width="3.4" height="6" rx=".6" fill="#fff"/></svg>
        +244 222 410 600
      </li>
      <li class="contact__item">
        <svg class="contact__icon" viewBox="0 0 10 10"><circle cx="5" cy="5" r="5" fill="#a3141c"/><rect x="2.5" y="3.2" width="5" height="3.8" fill="#fff"/></svg>
        +244 222 410 600
      </li>
      <li class="contact__item">
        <svg class="contact__icon" viewBox="0 0 10 10"><circle cx="5" cy="5" r="5" fill="#a3141c"/><path d="M2.5 3.2h5v3.6h-5z M2.5 3.2L5 5.2 7.5 3.2" fill="none" stroke="#fff" stroke-width=".8"/></svg>
        info@halvorn.co
      </li>
      <li class="contact__item">
        <svg class="contact__icon" viewBox="0 0 10 10"><circle cx="5" cy="5" r="5" fill="#a3141c"/><circle cx="5" cy="5" r="2.4" fill="none" stroke="#fff" stroke-width=".8"/><path d="M2.6 5h4.8" stroke="#fff" stroke-width=".6"/></svg>
        www.halvorn.co
      </li>
      <li class="contact__item">
        <svg class="contact__icon" viewBox="0 0 10 10"><circle cx="5" cy="5" r="5" fill="#a3141c"/><path d="M5 8L3.2 5a2 2 0 1 1 3.6 0z" fill="#fff"/></svg>
        Rua das Acácias
      </li>
      <li class="contact__item contact__item--plain">Luanda, Angola</li>
    </ul>

    <div class="brand">
      <span class="brand__mark"></span>
      <span class="brand__name">Halvorn Corporation</span>
    </div>
  </main>
</body>
</html>
```